A website for a Maltese Law Firm

Our law firm needs a website to further its business. The site should have a simple yet effective design. We would need the following sections: About us, Practice Areas, About Malta, Contact. These should be further split as follows:

About us: Our firm, Our values, What others say, Offices

Practice Areas: Crimimal, Citizenship & Residence, Overseas Patron Scheme, Criminal Defence, Civil Litigation, Arbitration and ADR, Commercial and Corporate, Media Law.

About Malta: just one section.

Contact: Just one section

We would also need a news feed at the front of the site to include latest news regarding our cases.

At the bottom we need a section for our Terms and a Privacy Statement.

Our logo is being attached.

Target Market(s)

All clients looking for legal assistance in Malta

Industry/Entity Type

Legal

Coding

Coded - Design and coding required

Number of Pages Required

1 page

Requirements
Must have
• It must be simple yet striking.

```html
<!DOCTYPE html>
<html lang="en">
<head>
<meta charset="utf-8">
<title>Castellane &amp; Rovero Advocates</title>
<link href="https://fonts.googleapis.com/css2?family=Roboto:wght@300;400;500;700&family=Nothing+You+Could+Do&display=swap" rel="stylesheet">
<style>
:root{
  --ink:#222;
  --text:#555;
  --muted:#777;
  --rule:#d9dbde;
  --panel:#f3f4f6;
  --brown:#3a2218;
  --navy:#0f4a6b;
  --footer:#30353b;
  --footer-text:#b7bcc2;
  --white:#fff;
}
*{box-sizing:border-box;margin:0;padding:0}
html,body{width:1200px;height:2667px;overflow:hidden}
body{font-family:"Roboto",Arial,sans-serif;color:var(--ink);background:var(--white);position:relative}

/* header */
.site-header{position:absolute;left:0;top:0;width:1200px;height:69px;background:var(--white)}
.brand{position:absolute;left:52px;top:12px;width:318px;border-top:2px solid var(--ink);border-bottom:2px solid var(--ink);padding:7px 0 6px;font-size:17px;line-height:20px;font-weight:400;letter-spacing:0.8px;text-transform:uppercase;color:var(--ink);text-align:center;white-space:nowrap}
.main-nav a{position:absolute;top:26px;font-size:13px;color:var(--ink);text-decoration:none;text-transform:uppercase;white-space:nowrap}
.login{position:absolute;left:1104px;top:0;width:44px;height:69px;background:var(--brown);color:var(--white);font-size:12px;font-weight:700;display:flex;align-items:center;justify-content:center;text-decoration:none}

/* hero */
.hero{position:absolute;left:0;top:69px;width:1200px;height:493px;background:linear-gradient(120deg,#3e4a57 0%,#5b6874 45%,#46525e 100%)}
.hero-title{position:absolute;left:222px;top:52px;font-family:"Nothing You Could Do",cursive;font-size:76px;line-height:74px;font-weight:400;color:var(--white)}
.hero-lead{position:absolute;left:224px;top:302px;font-size:20px;line-height:30px;font-weight:500;color:var(--white)}
.hero-btn{position:absolute;top:381px;height:32px;padding:0 14px;background:var(--white);color:var(--ink);font-size:10px;font-weight:700;display:flex;align-items:center;border-radius:2px}
.dots{position:absolute;left:566px;top:458px;display:flex;gap:8px}
.dots span{width:9px;height:9px;border-radius:50%;background:var(--white)}
.dots span.off{background:transparent;border:1.5px solid var(--white)}

/* stats */
.stat{position:absolute;top:572px;width:346px;text-align:center}
.stat h3{font-size:19px;font-weight:400;color:var(--ink)}
.stat .num{font-size:44px;font-weight:500;margin-top:14px}
.stat p{font-size:12px;line-height:18px;color:var(--text);margin-top:22px}

/* about panel */
.about{position:absolute;left:0;top:775px;width:1200px;height:368px;background:var(--panel)}
.section-title{position:absolute;font-size:21px;font-weight:700;color:var(--ink)}
.section-rule{position:absolute;height:0;border-top:1px dashed var(--rule)}
.feature{position:absolute;top:105px;width:360px;text-align:center}
.feature .icon{width:74px;height:80px;margin:0 auto;background:var(--ink);display:flex;align-items:center;justify-content:center}
.feature h4{font-size:17px;font-weight:700;margin-top:12px}
.feature p{width:334px;margin:14px auto 0;font-size:12px;line-height:19.5px;color:var(--text)}

/* practice */
.practice-image{position:absolute;left:52px;top:1291px;width:533px;height:373px;background:linear-gradient(150deg,#2b3550 0%,#1a2236 55%,#2f3a56 100%)}
.areas{position:absolute;left:617px;top:1310px;list-style:none}
.areas li{height:56px;display:flex;align-items:flex-start;font-size:16px;color:#333}
.areas .chev{width:22px;height:22px;background:#eceef1;margin-right:16px;display:flex;align-items:center;justify-content:center;margin-top:-2px}

/* news */
.card{position:absolute;top:1845px;width:254px;height:436px;background:var(--panel)}
.card .thumb{height:187px}
.card h3{font-size:18px;line-height:23px;font-weight:700;margin:14px 40px 0 20px}
.card p{font-size:13px;line-height:19px;color:var(--text);margin:8px 22px 0 20px;display:-webkit-box;-webkit-box-orient:vertical;-webkit-line-clamp:6;overflow:hidden}
.card p.short{-webkit-line-clamp:5}
.card .date{position:absolute;left:20px;right:20px;top:396px;border-top:1px solid var(--rule);padding-top:12px;font-size:11px;color:var(--text)}
.view-more{position:absolute;left:538px;top:2293px;width:109px;height:37px;background:var(--navy);color:var(--white);font-size:12px;font-weight:700;display:flex;align-items:center;justify-content:center}

/* footer */
.site-footer{position:absolute;left:0;top:2348px;width:1200px;height:319px;background:var(--footer)}
.f-col{position:absolute;top:56px;width:250px;color:var(--footer-text);font-size:12.5px;line-height:20px}
.f-col h4{font-size:17px;font-weight:700;color:var(--white);margin-bottom:20px}
.f-col p+p{margin-top:16px}
.f-col .label{color:var(--white);font-weight:400}
.social{width:10px;height:10px;border:1.5px solid var(--footer-text);margin-top:22px}
.f-rule{position:absolute;left:52px;top:248px;width:1096px;border-top:1px solid #444a51}
.copy{position:absolute;left:52px;top:276px;font-size:12px;color:var(--footer-text)}
</style>
</head>
<body>

<header class="site-header">
  <div class="brand">Castellane &amp; Rovero Advocates</div>
  <nav class="main-nav">
    <a style="left:542px">About us</a>
    <a style="left:642px">Our firm</a>
    <a style="left:741px">Practice areas</a>
    <a style="left:884px">About Malta</a>
    <a style="left:1008px">Contact</a>
  </nav>
  <a class="login">LOGIN</a>
</header>

<section class="hero" role="img" aria-label="Photograph of hands reviewing business charts and reports on a desk">
  <h1 class="hero-title">Customer<br>Oriented<br>Culture</h1>
  <p class="hero-lead">We offer quantitative and qualitative<br>solutions tailored to our clients' needs</p>
  <span class="hero-btn" style="left:224px">OUR SERVICES</span>
  <span class="hero-btn" style="left:346px">OUR WORK</span>
  <div class="dots"><span></span><span></span><span class="off"></span><span></span></div>
</section>

<section>
  <div class="stat" style="left:51px"><h3>Days of Work</h3><div class="num">3541 +</div><p>Lorem ipsum dolor sit amet, consectetur adipiscing elit, sed<br>do eiusmod tempor incididunt ut labore et.</p></div>
  <div class="stat" style="left:428px"><h3>Satisfied Clients</h3><div class="num">100 +</div><p>Lorem ipsum dolor sit amet, consectetur adipiscing elit, sed<br>do eiusmod tempor incididunt ut labore et.</p></div>
  <div class="stat" style="left:801px"><h3>Finished Projects</h3><div class="num">240 +</div><p>Lorem ipsum dolor sit amet, consectetur adipiscing elit, sed<br>do eiusmod tempor incididunt ut labore et.</p></div>
</section>

<section class="about">
  <h2 class="section-title" style="left:40px;top:26px">Castellane &amp; Rovero Advocates</h2>
  <div class="section-rule" style="left:40px;top:64px;width:1124px"></div>
  <div class="feature" style="left:45px">
    <div class="icon"><svg width="44" height="44" viewBox="0 0 44 44" fill="none" stroke="#fff" stroke-width="1.6"><line x1="22" y1="6" x2="22" y2="36"/><line x1="8" y1="11" x2="36" y2="11"/><line x1="14" y1="38" x2="30" y2="38"/><path d="M8 11 L3 24 H13 Z"/><path d="M36 11 L31 24 H41 Z"/><path d="M3 24 Q8 30 13 24"/><path d="M31 24 Q36 30 41 24"/></svg></div>
    <h4>Our firm</h4>
    <p>The quality perception of the product, what clients would like to change, what price can they afford, where is this product wanted the most, what causes dissatisfaction in a product (i.e. price, quality,design)</p>
  </div>
  <div class="feature" style="left:420px">
    <div class="icon"><svg width="44" height="44" viewBox="0 0 44 44" fill="none" stroke="#fff" stroke-width="1.6"><path d="M22 5 L27 17 L40 18 L30 26 L33 39 L22 32 L11 39 L14 26 L4 18 L17 17 Z" stroke-linejoin="round"/></svg></div>
    <h4>Our values</h4>
    <p>CRadvocates is a team of law firm that work toward delivering law services while upholding the highest standards of design, analysis and reporting. Our mission is to help business in law firm</p>
  </div>
  <div class="feature" style="left:795px">
    <div class="icon"><svg width="44" height="44" viewBox="0 0 44 44" fill="none" stroke="#fff" stroke-width="1.6"><path d="M11 5 H27 L34 12 V39 H11 Z"/><path d="M27 5 V12 H34"/><line x1="16" y1="19" x2="29" y2="19"/><line x1="16" y1="24" x2="29" y2="24"/><line x1="16" y1="29" x2="29" y2="29"/><line x1="16" y1="34" x2="25" y2="34"/></svg></div>
    <h4>Our Offices</h4>
    <p>Our vision is to be a long-term preferred partner to our clients in the field of market law and business consulting. We are relentlessly focused on delivering exceptional value in provision of strategy, law and analysis</p>
  </div>
</section>

<section>
  <h2 class="section-title" style="left:52px;top:1214px">Practice Areas</h2>
  <div class="section-rule" style="left:52px;top:1253px;width:1096px"></div>
  <div class="practice-image" role="img" aria-label="Photograph looking up at classical stone columns of a courthouse"></div>
  <ul class="areas">
    <li><span class="chev"><svg width="10" height="6" viewBox="0 0 10 6"><path d="M1 1 L5 5 L9 1" fill="none" stroke="#555" stroke-width="1.4"/></svg></span>Crimimal</li>
    <li><span class="chev"><svg width="10" height="6" viewBox="0 0 10 6"><path d="M1 1 L5 5 L9 1" fill="none" stroke="#555" stroke-width="1.4"/></svg></span>Citizenship &amp; Residence</li>
    <li><span class="chev"><svg width="10" height="6" viewBox="0 0 10 6"><path d="M1 1 L5 5 L9 1" fill="none" stroke="#555" stroke-width="1.4"/></svg></span>Overseas Patron Scheme</li>
    <li><span class="chev"><svg width="10" height="6" viewBox="0 0 10 6"><path d="M1 1 L5 5 L9 1" fill="none" stroke="#555" stroke-width="1.4"/></svg></span>Criminal Defence</li>
    <li><span class="chev"><svg width="10" height="6" viewBox="0 0 10 6"><path d="M1 1 L5 5 L9 1" fill="none" stroke="#555" stroke-width="1.4"/></svg></span>Civil Litigation</li>
    <li><span class="chev"><svg width="10" height="6" viewBox="0 0 10 6"><path d="M1 1 L5 5 L9 1" fill="none" stroke="#555" stroke-width="1.4"/></svg></span>Arbitration and ADR</li>
    <li><span class="chev"><svg width="10" height="6" viewBox="0 0 10 6"><path d="M1 1 L5 5 L9 1" fill="none" stroke="#555" stroke-width="1.4"/></svg></span>Commercial and Corporate</li>
  </ul>
</section>

<section>
  <h2 class="section-title" style="left:52px;top:1748px">Latest News</h2>
  <div class="section-rule" style="left:52px;top:1787px;width:1096px"></div>

  <article class="card" style="left:52px">
    <div class="thumb" style="background:#e21e26" role="img" aria-label="Partner charity emblem on a red background"></div>
    <h3>Citizen Friendly Budgets and Budget Analysis for Children</h3>
    <p class="short">In cooperation with Kindlebrook Trust, Vendral Consulting has drafted the Citizen Friendly Budgets and Budget Analysis for Children in the Municipalities of Dravenik and Solmira...</p>
    <div class="date">11 February, 2016</div>
  </article>
  <article class="card" style="left:332px">
    <div class="thumb" style="background:linear-gradient(160deg,#8a8d8c,#3d4240)" role="img" aria-label="Photograph of participants seated at a training session"></div>
    <h3>Community Needs Assessment Training</h3>
    <p>Vendral Consulting is conducting a two-day training on Community Needs Assessment. This two-day training was commissioned by Orlaine organization, and it is being delivered...</p>
    <div class="date">23 December, 2015</div>
  </article>
  <article class="card" style="left:613px">
    <div class="thumb" style="background:linear-gradient(160deg,#c9c4b4,#5a5a55)" role="img" aria-label="Photograph of a presentation launch event in a conference hall"></div>
    <h3>Mapping of ICT Sector Labor Supply</h3>
    <p>Today during the Qorvessa Education launch event, Vendral Consulting presented the findings of the study on "Mapping of ICT Sector Labor Supply and Demand"...</p>
    <div class="date">15 December, 2015</div>
  </article>
  <article class="card" style="left:894px">
    <div class="thumb" style="background:linear-gradient(160deg,#c7a58a,#5a4236)" role="img" aria-label="Photograph of a speaker presenting study findings at a lectern"></div>
    <h3>Study on Impact and Sustainability of Learning Centres</h3>
    <p>Vendral Consulting presented today the findings from the "Study on Impact and Sustainability of Learning Centres" to governmental representatives, international...</p>
    <div class="date">3 December, 2015</div>
  </article>

  <span class="view-more">VIEW MORE</span>
</section>

<footer class="site-footer">
  <div class="f-col" style="left:52px">
    <h4>Contact</h4>
    <p>Please feel free to contact us for any issue. Our staff is available to you from 9AM until 5PM on weekdays.</p>
    <div class="social"></div>
  </div>
  <div class="f-col" style="left:332px">
    <h4>Phone number</h4>
    <p><span class="label">Valletta:</span> (356) 2100 1234</p>
    <p><span class="label">Birkirkara:</span> (356) 2100 5678</p>
  </div>
  <div class="f-col" style="left:613px">
    <h4>Office</h4>
    <p><span class="label">Office 1:</span> 12/4 Harbour Lane, Valletta</p>
    <p><span class="label">Office 2:</span> 58 Olive Street, Birkirkara</p>
  </div>
  <div class="f-col" style="left:894px">
    <h4>E-Mail</h4>
    <p><span class="label">Info:</span> info@cradvocates.example</p>
  </div>
  <div class="f-rule"></div>
  <div class="copy">© 2001-2016 CRadvocates</div>
</footer>

</body>
</html>
```